International Accounting, Law and Real Estate firm needs a English-Spanish web design

We are a firm dedicated to accounting-taxes, Legal and Real Estate in the northern part of Mexico on the border with Arizona USA, so our clients are half Mexicans and Half Americans. We are located on the coast (Puerto Peñasco, also called Rocky Point). Our name is NOVA ADVISORY, where REAL stands for:
R=real
E= estate
A= Accounting
L= Legal
our web page is www.novaadvisory-demo.com.mx, we need something more attractive, profesional, fresh, inviting, and we need to have it in English and a Spanish and I need to be able to keep uploading new properties for sale.
Our number one activity now is Accounting and Taxes, we are growing on the legal side and there is a huge opportunity in the market to help Foreigners get their property titles, and our third activity is Real Estate. We have an excellent reputation of honesty and professional people. We would like to advertise as a ONE PLACE for Legal and Taxes matters. Or also something like Your Taxes and Trust specialists... or Total solutions with Integrity ....

Target Market(s)

local business and US visitors some of them do business in Mexico, others buy properties and need legal help to be able to get their title (which is done by a trust)

Industry/Entity Type

Real Estate

Number of Pages Required

3 page

Font styles to use
Serif
Sans Serif

Requirements
Must have
• Be in English and Spanish (I can help with translation English to Spanish); be able to update the real estate area since it changes accordingly to new listings and sales.
Nice to have
• Easy to navigate and to enter to each area of web page, we would have 3 areas the 1.- accounting and taxes
• 2.- Legal
• 3.- Real Estate

```html
<!DOCTYPE html>
<html lang="en">
<head>
<meta charset="utf-8">
<title>Nova Advisory — Real Estate, Accounting, Legal</title>
<link rel="stylesheet" href="https://fonts.googleapis.com/css2?family=Noto+Serif:wght@400;700&family=Dancing+Script:wght@400;700&family=Kaushan+Script&display=swap">
<style>
  :root {
    --orange: #f7941d;
    --orange-deep: #f58a1f;
    --yellow: #fcc13b;
    --magenta: #9e1f63;
    --magenta-light: #c0397a;
    --blue: #1c6fae;
    --blue-light: #3a95d2;
    --ink: #2b2b2b;
    --grey-text: #8c8c8c;
    --white: #ffffff;
    --bar-top: #f2f2f2;
    --bar-mid: #8e8e8e;
    --bar-low: #c9c9c9;
    --serif: "Noto Serif", Georgia, serif;
  }
  * { box-sizing: border-box; margin: 0; padding: 0; }
  html, body { width: 735px; height: 1200px; overflow: hidden; background: var(--white); }
  .page { position: relative; width: 735px; height: 1200px; font-family: var(--serif); color: var(--ink); overflow: hidden; }

  /* Header */
  .header-decor { position: absolute; top: 18px; height: 120px; width: 150px;
    background: linear-gradient(90deg, rgba(248,196,220,.55), rgba(191,220,240,.55), rgba(252,236,170,.55)); border-radius: 6px; }
  .header-decor.left { left: 102px; }
  .header-decor.right { left: 480px; }
  .brand { position: absolute; top: 70px; left: 0; width: 735px; text-align: center; }
  .brand-line { line-height: 26px; }
  .brand-mark { display: inline-block; width: 16px; height: 16px; background: var(--orange); vertical-align: -1px; margin-right: 6px; }
  .brand-name { font-size: 20px; font-weight: 700; color: var(--orange); letter-spacing: .3px; }
  .brand-tagline { margin-top: 1px; font-size: 7.5px; line-height: 10px; font-weight: 700; color: var(--blue); letter-spacing: .6px; }
  .top-nav { position: absolute; top: 127px; left: 0; width: 735px; text-align: center; font-size: 12px; color: var(--grey-text); letter-spacing: .5px; }
  .top-nav span.sep { margin: 0 9px; }
  .call-us { position: absolute; top: 104px; right: 12px; text-align: right; font-size: 12.5px; line-height: 17px; color: var(--grey-text); }

  /* Section tabs */
  .tabs { position: absolute; top: 170px; left: 0; width: 735px; height: 34px; }
  .tab { position: absolute; top: 0; height: 34px; border-radius: 14px 14px 0 0; color: var(--white);
    font-size: 12.5px; text-transform: uppercase; letter-spacing: .3px; text-align: center; line-height: 34px; }
  .tab.accounting { left: 170px; width: 168px; background: linear-gradient(var(--magenta-light), var(--magenta)); }
  .tab.legal { left: 375px; width: 168px; background: linear-gradient(var(--blue-light), var(--blue)); }
  .tab.realestate { left: 562px; width: 173px; background: linear-gradient(#fbab3c, var(--orange)); border-radius: 14px 0 0 0; }
  .section-bar { position: absolute; top: 204px; left: 0; width: 735px; height: 46px;
    background: linear-gradient(var(--bar-top), var(--bar-mid) 55%, var(--bar-low)); }

  /* Hero */
  .hero { position: absolute; top: 267px; left: 0; width: 735px; height: 408px;
    background: linear-gradient(180deg, #6f9fd0 0%, #b7d1ea 28%, #d9d2c0 45%, #2f87a8 58%, #4aa4bd 75%, #d8cdb5 100%); }
  .hero-word { position: absolute; font-family: "Dancing Script", cursive; color: rgba(255,255,255,.55); font-size: 66px; }
  .hero-word.es { left: 28px; top: 272px; }
  .hero-word.en { left: 282px; top: 326px; }

  /* Team */
  .team-photo { position: absolute; background: linear-gradient(160deg, #e9d7c8, #b98e72); }
  .team-photo.first { left: 87px; top: 693px; width: 90px; height: 122px; }
  .team-photo.second { left: 99px; top: 858px; width: 66px; height: 110px; background: linear-gradient(160deg, #8d8d8d, #3f3f3f); }
  .team-name { position: absolute; left: 20px; width: 225px; text-align: center; font-size: 11.5px; font-weight: 700; line-height: 15px; }
  .team-name.first { top: 824px; }
  .team-name.second { top: 979px; font-size: 10.5px; }

  .intro { position: absolute; left: 267px; top: 703px; width: 425px; font-size: 13.5px; line-height: 19.3px;
    hyphens: auto; -webkit-hyphens: auto; }
  .motto { position: absolute; left: 267px; top: 858px; width: 425px; text-align: center; font-size: 13.5px; line-height: 19px; }
  .welcome { position: absolute; left: 267px; top: 900px; width: 425px; text-align: center;
    font-family: "Kaushan Script", cursive; font-size: 30px; line-height: 42px; color: #111; }

  /* Footer */
  .footer { position: absolute; top: 1030px; left: 0; width: 735px; height: 170px;
    background: linear-gradient(var(--orange-deep), var(--orange) 35%, var(--yellow)); color: var(--white); }
  .footer-brand { position: absolute; left: 22px; top: 8px; font-size: 20px; line-height: 22px; font-weight: 700; letter-spacing: .4px; }
  .footer-tagline { position: absolute; left: 22px; top: 31px; font-size: 7.5px; line-height: 9px; font-weight: 700; letter-spacing: .6px; }
  .field { position: absolute; height: 24px; background: var(--white); border: 1.5px solid #7a4a10;
    font-size: 11px; color: #999; padding-left: 12px; line-height: 21px; letter-spacing: .5px; }
  .field.login { left: 22px; top: 45px; width: 208px; }
  .field.password { left: 22px; top: 84px; width: 208px; }
  .field.subscribe { left: 267px; top: 45px; width: 205px; }
  .footer-heading { position: absolute; top: 15px; font-size: 12px; line-height: 15px; letter-spacing: .4px; text-transform: uppercase; }
  .footer-heading.subscribe { left: 277px; }
  .footer-heading.comments { left: 510px; width: 195px; text-align: center; }
  .recent-comment { position: absolute; left: 505px; top: 40px; width: 205px; text-align: center; font-size: 11px; line-height: 14px; letter-spacing: .3px; }
</style>
</head>
<body>
<div class="page">
  <header>
    <div class="header-decor left" role="img" aria-label="Soft pastel geometric decoration"></div>
    <div class="header-decor right" role="img" aria-label="Soft pastel geometric decoration"></div>
    <div class="brand">
      <div class="brand-line"><span class="brand-mark"></span><span class="brand-name">NOVA ADVISORY</span></div>
      <div class="brand-tagline">REAL ESTATE, ACCOUNTING, LEGAL</div>
    </div>
    <nav class="top-nav">CONTACT<span class="sep">|</span>ABOUT<span class="sep">|</span>BLOG</nav>
    <div class="call-us">Call Us:<br>US (555) 014 2290<br>MX (555) 017 6631</div>
  </header>

  <nav class="tabs">
    <div class="tab accounting">Accounting and Taxes</div>
    <div class="tab legal">Legal</div>
    <div class="tab realestate">Real Estate</div>
  </nav>
  <div class="section-bar"></div>

  <section class="hero" role="img" aria-label="Aerial photo of beachfront condominium towers on the coast">
    <span class="hero-word es">bienvenida</span>
    <span class="hero-word en">welcome</span>
  </section>

  <section class="team">
    <div class="team-photo first" role="img" aria-label="Portrait photo of the firm's CPA"></div>
    <div class="team-name first">CPA Lena Ortiz</div>
    <div class="team-photo second" role="img" aria-label="Portrait photo of the firm's attorney"></div>
    <div class="team-name second">Atty. Marco Ibarra (MBA, Corporate<br>and Real Estate Attorney at Law)</div>
  </section>

  <section>
    <p class="intro">We are a team of professionals advising our national and international clients doing business in Mexico. We are a creative firm that prides itself on finding the best bespoke solutions for our clients. If the obvious doesn’t work, we always look for other ways of getting a result; it’s a natural aspect of how our people work putting in front our professionalism and integrity which are the soul of our company.</p>
    <p class="motto">Our people make the difference!!</p>
    <p class="welcome">Welcome, we look forward to<br>serving you!</p>
  </section>

  <footer class="footer">
    <div class="footer-brand">NOVA ADVISORY</div>
    <div class="footer-tagline">REAL ESTATE, ACCOUNTING, LEGAL</div>
    <div class="field login">LOGIN</div>
    <div class="field password">PASSWORD</div>
    <div class="footer-heading subscribe">Subscribe to blog via email</div>
    <div class="field subscribe"></div>
    <div class="footer-heading comments">Recent comments</div>
    <div class="recent-comment">MARCO IBARRA ON DEMO POST 2</div>
  </footer>
</div>
</body>
</html>
```